Draft Beer System Services Sales Sheet

Wanting a sales sheet (leave behind) to match the glycol chiller maintenance sales sheet you created earlier this year (.pdf attached) for our company. I will upload a sketch with dialogue. I will also upload some relevant images. Can't wait to see this come together.

Target Market(s)

Bars, Brewery Tap Rooms, Restaurants, Sporting Venues

Industry/Entity Type

Draft Beer and Brewery Services

Font styles to use
Serif

Requirements
Must have
• Similar theme as previous sales sheet
Nice to have
• Images that seem relevant

```html
<!DOCTYPE html>
<html lang="en">
<head>
<meta charset="utf-8">
<title>Draft Beer System Services</title>
<link href="https://fonts.googleapis.com/css2?family=Anton&family=Bebas+Neue&display=swap" rel="stylesheet">
<style>
  :root {
    --orange: #f9a61a;
    --orange-deep: #f08a1d;
    --orange-light: #fdb94a;
    --brown: #b45a12;
    --charcoal: #232323;
    --gear: #2b2b2b;
    --grey-light: #e4e4e4;
    --grey-mid: #c2c2c2;
    --logo-ink: #6a6a6a;
    --white: #ffffff;
  }
  * { margin: 0; padding: 0; box-sizing: border-box; }
  html, body { width: 848px; height: 1200px; overflow: hidden; background: var(--white); }
  .sheet { position: relative; width: 848px; height: 1200px; overflow: hidden; background: var(--white); }
  .hero-art { position: absolute; left: 0; top: 0; width: 848px; height: 600px; }

  .brand-card {
    position: absolute; left: 25px; top: 0; width: 228px; height: 179px;
    border-radius: 0 0 28px 28px;
    background: linear-gradient(135deg, var(--grey-mid), var(--grey-light) 55%, #d0d0d0);
    box-shadow: 0 3px 8px rgba(0,0,0,.25);
    display: flex; align-items: center; justify-content: center; gap: 8px;
  }
  .brand-card .brand-dot { width: 16px; height: 16px; border-radius: 50%; background: var(--logo-ink); }
  .brand-card .brand-name {
    font-family: "Bebas Neue", sans-serif; font-size: 38px; color: var(--logo-ink); letter-spacing: 1px;
  }

  .headline {
    position: absolute; left: 25px; top: 278px;
    font-family: "Anton", sans-serif; font-size: 56px; line-height: 1; letter-spacing: 0.5px;
    color: var(--charcoal);
  }
  .headline .accent { color: var(--white); }
  .subhead-pill {
    position: absolute; left: 0; top: 346px; width: 288px; height: 58px;
    border-radius: 0 29px 29px 0;
    background: linear-gradient(90deg, var(--grey-light), #d6d6d6);
    display: flex; align-items: center; padding-left: 24px;
    font-family: "Anton", sans-serif; font-size: 33px; color: var(--charcoal);
  }

  .services-panel {
    position: absolute; left: 25px; top: 620px; width: 799px; height: 470px;
    border-radius: 52px; background: var(--charcoal); overflow: hidden;
  }
  .services-panel .gears { position: absolute; left: 0; top: 0; width: 799px; height: 470px; }
  .service-tab {
    position: absolute; left: 0; width: 250px; height: 53px;
    border-radius: 0 27px 27px 0; background: var(--orange);
    font-family: "Bebas Neue", sans-serif; font-size: 34px; line-height: 53px;
    color: var(--charcoal); padding-left: 71px; padding-top: 2px;
  }
  .service-copy {
    position: absolute; left: 71px; width: 630px;
    font-family: "Bebas Neue", sans-serif; font-size: 20px; line-height: 24.5px;
    color: var(--white);
  }

  .footer-band { position: absolute; left: 0; top: 1124px; width: 848px; height: 76px; background: var(--charcoal); }
  .footer-tab {
    position: absolute; left: 0; top: 1109px; width: 290px; height: 140px;
    border-radius: 0 48px 48px 0; background: var(--orange);
    box-shadow: 4px 0 8px rgba(0,0,0,.2);
  }
</style>
</head>
<body>
<main class="sheet">
  <svg class="hero-art" viewBox="0 0 848 600" aria-hidden="false">
    <defs>
      <linearGradient id="tapsTone" x1="0" y1="0" x2="1" y2="1">
        <stop offset="0" stop-color="#5b4a3c"/>
        <stop offset="0.35" stop-color="#a2714a"/>
        <stop offset="0.65" stop-color="#c9c9c9"/>
        <stop offset="1" stop-color="#8e959c"/>
      </linearGradient>
    </defs>
    <path class="hero-orange" fill="var(--orange)" d="M0 0 H848 V420 L440 456 C260 468 100 515 0 575 Z"/>
    <path class="swoosh-brown" fill="var(--brown)" d="M0 565 C110 505 270 462 420 456 C270 470 120 520 0 585 Z"/>
    <path class="swoosh-orange" fill="var(--orange-deep)" d="M0 585 C120 520 280 470 420 458 C280 478 130 535 0 605 Z"/>
    <path class="swoosh-light" fill="var(--orange-light)" d="M0 605 C130 535 290 480 400 462 C280 490 130 555 0 625 Z"/>
    <circle fill="var(--orange-light)" cx="650" cy="258" r="297"/>
    <circle fill="var(--white)" cx="658" cy="250" r="290"/>
    <circle fill="var(--orange-deep)" cx="664" cy="245" r="285"/>
    <circle fill="var(--orange)" cx="664" cy="240" r="280"/>
    <circle role="img" aria-label="Photo of a row of chrome draft beer faucets with wooden tap handles" fill="url(#tapsTone)" cx="664" cy="235" r="277"/>
  </svg>

  <div class="brand-card">
    <span class="brand-dot"></span>
    <span class="brand-name">Tapline Crew</span>
  </div>

  <h1 class="headline">DRAFT <span class="accent">BEER</span></h1>
  <div class="subhead-pill">SYSTEM SERVICES</div>

  <section class="services-panel">
    <svg class="gears" viewBox="0 0 799 470" aria-hidden="true">
      <g fill="var(--gear)">
        <g transform="translate(609 328)">
          <circle r="70"/>
          <rect x="-16" y="-86" width="32" height="172" rx="4"/>
          <rect x="-16" y="-86" width="32" height="172" rx="4" transform="rotate(45)"/>
          <rect x="-16" y="-86" width="32" height="172" rx="4" transform="rotate(90)"/>
          <rect x="-16" y="-86" width="32" height="172" rx="4" transform="rotate(135)"/>
        </g>
        <g transform="translate(736 396)">
          <circle r="38"/>
          <rect x="-9" y="-47" width="18" height="94" rx="3"/>
          <rect x="-9" y="-47" width="18" height="94" rx="3" transform="rotate(45)"/>
          <rect x="-9" y="-47" width="18" height="94" rx="3" transform="rotate(90)"/>
          <rect x="-9" y="-47" width="18" height="94" rx="3" transform="rotate(135)"/>
        </g>
      </g>
      <circle fill="var(--charcoal)" cx="609" cy="328" r="34"/>
      <circle fill="var(--charcoal)" cx="736" cy="396" r="13"/>
    </svg>
  </section>

  <div class="service-tab" style="top:633px">SYSTEM DESIGN</div>
  <p class="service-copy" style="top:700px">LOREM IPSUM DOLOR SIT AMET, CONSECTETUR ADIPISCING ELIT, SED DO EIUSMOD TEMPOR INCIDIDUNT UT LABORE ET DOLORE MAGNA ALIQUA. QUIS IPSUM SUSPENDISSE ULTRICES GRAVIDA. RISUS COMMODO VIVERRA MAECENAS ACCUMSAN LACUS VEL FACILISIS.</p>

  <div class="service-tab" style="top:785px">SYSTEM DESIGN</div>
  <p class="service-copy" style="top:850px">LOREM IPSUM DOLOR SIT AMET, CONSECTETUR ADIPISCING ELIT, SED DO EIUSMOD TEMPOR INCIDIDUNT UT LABORE ET DOLORE MAGNA ALIQUA. QUIS IPSUM SUSPENDISSE ULTRICES GRAVIDA. RISUS COMMODO VIVERRA MAECENAS ACCUMSAN LACUS VEL FACILISIS.</p>

  <div class="service-tab" style="top:935px">SYSTEM DESIGN</div>
  <p class="service-copy" style="top:998px">LOREM IPSUM DOLOR SIT AMET, CONSECTETUR ADIPISCING ELIT, SED DO EIUSMOD TEMPOR INCIDIDUNT UT LABORE ET DOLORE MAGNA ALIQUA. QUIS IPSUM SUSPENDISSE ULTRICES GRAVIDA. RISUS COMMODO VIVERRA MAECENAS ACCUMSAN LACUS VEL FACILISIS.</p>

  <div class="footer-band"></div>
  <div class="footer-tab"></div>
</main>
</body>
</html>
```